Bramblewood Lodging letterhead

We need a letterhead designed that includes the new logo that has just been designed for our business. The letterhead will need to be formatted for digital use as well as for print.

Target Market(s)

Private tenant, corporate tenants, real estate agents

Industry/Entity Type

Digital

Requirements
Must have
• ABN 87 592 104 316
PO Box 7816, Tilbury Mail Centre QLD 4792
Email: dorian.platt@quillmail.net
Ph: 0438 172 964

```html
<!DOCTYPE html>
<html lang="en">
<head>
<meta charset="utf-8">
<title>Bramblewood Lodging Letterhead</title>
<link href="https://fonts.googleapis.com/css2?family=Dosis:wght@600;700&display=swap" rel="stylesheet">
<style>
  :root {
    --brand-maroon: #7b2a28;
    --brand-red: #8c2d22;
    --header-grey: #f4f4f4;
    --page-white: #ffffff;
    --frame-grey: #6f6f6f;
    --mark-faint: #f3eeec;
    --mark-faint-text: #e6dcd9;
  }
  html, body {
    margin: 0;
    padding: 0;
    width: 849px;
    height: 1200px;
    overflow: hidden;
    background: var(--page-white);
  }
  .letterhead {
    position: relative;
    width: 849px;
    height: 1200px;
    box-sizing: border-box;
    border: 1.5px solid var(--frame-grey);
    background: var(--page-white);
    overflow: hidden;
    font-family: "Dosis", "Trebuchet MS", sans-serif;
  }
  .header-band {
    position: absolute;
    top: 0;
    left: 0;
    width: 849px;
    height: 240px;
  }
  .brand {
    position: absolute;
    top: 26px;
    left: 14px;
    display: flex;
    align-items: center;
    gap: 12px;
  }
  .brand-square {
    width: 74px;
    height: 74px;
    border-radius: 8px;
    background: var(--brand-maroon);
  }
  .brand-name {
    font-weight: 700;
    font-size: 30px;
    line-height: 1;
    color: var(--brand-maroon);
    letter-spacing: 0.3px;
  }
  .contact-details {
    position: absolute;
    top: 30px;
    left: 556px;
    margin: 0;
    font-style: normal;
    font-weight: 600;
    font-size: 16.5px;
    line-height: 22.5px;
    color: var(--brand-red);
    white-space: nowrap;
  }
  .contact-details span { display: block; }
  .watermark {
    position: absolute;
    left: 324px;
    top: 494px;
    width: 201px;
    height: 211px;
    border-radius: 22px;
    background: var(--mark-faint);
    display: flex;
    align-items: center;
    justify-content: center;
    text-align: center;
    font-weight: 700;
    font-size: 26px;
    line-height: 1.1;
    color: var(--mark-faint-text);
  }
</style>
</head>
<body>
  <div class="letterhead">
    <svg class="header-band" viewBox="0 0 849 240" aria-hidden="true">
      <polygon points="0,0 849,0 849,235 422,118 0,235" fill="var(--header-grey)"/>
    </svg>

    <div class="brand">
      <div class="brand-square"></div>
      <div class="brand-name">Bramblewood<br>Lodging</div>
    </div>

    <address class="contact-details">
      <span>ABN 87 592 104 316</span>
      <span>PO BOX 7816 , Tilbury Mail Centre</span>
      <span>QLD 4792</span>
      <span>EMAIL : dorian.platt@quillmail.net</span>
      <span>PHONE : 0438 172 964</span>
    </address>

    <div class="watermark" aria-hidden="true">Bramblewood<br>Lodging</div>
  </div>
</body>
</html>
```